Harbor Lantern Bcard/Stationary
Harbor Lantern Advisory, LLC
Harbor Lantern Bcard/Stationary - Consulting
Creative Brief
Professional
Dana P. Whitcombe, AICP
Founder and Principal
4927 Corbel Street, Suite 300 Miami Beach, FL 33140
dana@harborlanternadvisory.example
https://harborlanternadvisory.example/
Please include Twitter handle on card: @msdanawhit
Include the logo either in color or in reverse. Would also like to see an option that includes the logo and this tag line: Creative Solutions for Evolving Places

```html
<!DOCTYPE html>
<html lang="en">
<head>
<meta charset="utf-8">
<title>Harbor Lantern Stationery Concepts</title>
<link href="https://fonts.googleapis.com/css2?family=Open+Sans:wght@400;600;700&display=swap" rel="stylesheet">
<style>
:root{
  --board:#3b3b3c;
  --board-dark:#2e2e2f;
  --paper:#ffffff;
  --ink:#3a3a3a;
  --muted:#8a8a8a;
  --purple:#6a2d8e;
  --orange:#f37a21;
  --green:#7bb647;
  --grey:#d9d9d9;
  --label:#c9c9c9;
}
*{box-sizing:border-box;margin:0;padding:0}
html,body{width:1200px;height:440px;overflow:hidden}
body{background:radial-gradient(ellipse at 50% 40%,var(--board),var(--board-dark));font-family:"Open Sans",Arial,sans-serif;color:var(--ink);position:relative}
.item{position:absolute;background:var(--paper);box-shadow:0 3px 8px rgba(0,0,0,.45)}
.label{position:absolute;font-size:6px;color:var(--label);text-align:center}
.brand{display:flex;align-items:center;gap:4px;font-weight:700;color:var(--purple);white-space:nowrap}
.brand .dot{border-radius:50%;background:var(--purple);flex:none}
.brand.rev{color:var(--paper)}
.brand.rev .dot{background:var(--paper)}
.stripe{position:absolute;left:0;right:0;bottom:0;height:4px;display:flex}
.stripe span{flex:1}
.s-p{background:var(--purple)}.s-o{background:var(--orange)}.s-g{background:var(--green)}.s-y{background:var(--grey)}

/* intro */
.intro{position:absolute;left:92px;top:160px;color:var(--paper)}
.intro .brand{font-size:15px}
.intro .brand .dot{width:16px;height:16px;background:var(--paper)}
.intro .brand{color:var(--paper)}
.intro .sub{font-size:7px;margin:2px 0 0 20px;color:var(--label)}
.intro .title{font-size:11px;margin:3px 0 0 20px}

/* business cards */
.card-front{display:flex}
.card-front .logo-side{flex:1;display:flex;align-items:center;justify-content:center}
.card-front .rows{width:55%;display:flex;flex-direction:column}
.card-front .rows div{flex:1;color:var(--paper);padding:0 5px;display:flex;flex-direction:column;justify-content:center;line-height:1.25}
.card-front .rows .r-y{color:var(--ink)}
.card-back{background:var(--purple);display:flex;flex-direction:column;align-items:center;justify-content:center}
.card-back .tag{color:var(--paper);opacity:.85}

/* letterhead */
.sheet{padding:14px 16px}
.sheet .head{display:flex;justify-content:space-between;align-items:flex-start}
.sheet .addr{font-size:4px;color:var(--muted);text-align:right;line-height:1.5}
.letter .body{font-size:4.2px;line-height:1.6;color:var(--ink);margin-top:20px}
.letter .body p{margin-bottom:5px}
.letter .sig{width:52px;height:14px;margin:4px 0 2px;background:linear-gradient(90deg,#e9e4ef,#f6f3f9)}

/* envelope */
.env{padding:8px 10px}
.env .addr{font-size:4px;color:var(--muted);line-height:1.5;margin-top:2px}

/* fax */
.fax table{width:100%;border-collapse:collapse;margin-top:18px;font-size:4.5px}
.fax td{border-bottom:0.6px solid var(--grey);padding:5px 2px;color:var(--ink)}
.fax .cm{font-size:4.5px;margin-top:10px;font-weight:600}
.fax .ring{position:absolute;right:14px;top:120px}
</style>
</head>
<body>

<section class="intro">
  <div class="brand"><span class="dot"></span>Harbor Lantern</div>
  <div class="sub">Advisory, LLC</div>
  <div class="title">Stationery Concepts</div>
</section>

<!-- front card, left column -->
<article class="item card-front" style="left:34px;top:240px;width:130px;height:78px">
  <div class="logo-side"><div class="brand" style="font-size:7px"><span class="dot" style="width:7px;height:7px"></span>Harbor Lantern</div></div>
  <div class="rows" style="font-size:3.6px">
    <div class="s-p"><b>Dana P. Whitcombe, AICP</b>Founder and Principal</div>
    <div class="s-o">4927 Corbel Street, Suite 300<br>Miami Beach, FL 33140</div>
    <div class="s-g">dana@harborlanternadvisory.example</div>
    <div class="r-y s-y">@msdanawhit</div>
  </div>
</article>
<div class="label" style="left:34px;top:322px;width:130px">Front Card</div>

<article class="item card-back" style="left:34px;top:340px;width:130px;height:78px">
  <div class="brand rev" style="font-size:9px"><span class="dot" style="width:9px;height:9px"></span>Harbor Lantern</div>
  <div class="tag" style="font-size:4px;margin-top:3px">Creative Solutions for Evolving Places</div>
</article>
<div class="label" style="left:34px;top:422px;width:130px">Back Card Option 1</div>

<!-- letterhead -->
<article class="item sheet letter" style="left:276px;top:36px;width:200px;height:380px">
  <div class="head">
    <div class="brand" style="font-size:7px"><span class="dot" style="width:8px;height:8px"></span>Harbor Lantern</div>
    <div class="addr">4927 Corbel Street, Suite 300<br>Miami Beach, FL 33140<br>dana@harborlanternadvisory.example<br>harborlanternadvisory.example</div>
  </div>
  <div class="body">
    <p><b>Recipient Name</b><br>Company Address Line</p>
    <p>Dear Recipient,</p>
    <p>Thank you for meeting with our team this week. We are pleased to share the planning outline we discussed, along with next steps.</p>
    <p>Our approach brings residents, leaders and designers together to shape places that grow with care and purpose over time.</p>
    <p>Please let us know a good time to talk.</p>
    <p>Sincerely,</p>
    <div class="sig" role="img" aria-label="Handwritten signature"></div>
    <p>Dana P. Whitcombe, AICP<br>Founder and Principal</p>
  </div>
  <div class="stripe"><span class="s-p"></span><span class="s-o"></span><span class="s-g"></span></div>
</article>
<div class="label" style="left:276px;top:422px;width:200px">Letterhead</div>

<!-- front card, large -->
<article class="item card-front" style="left:516px;top:100px;width:204px;height:116px">
  <div class="logo-side"><div class="brand" style="font-size:10px"><span class="dot" style="width:10px;height:10px"></span>Harbor Lantern</div></div>
  <div class="rows" style="font-size:5px">
    <div class="s-p"><b>Dana P. Whitcombe, AICP</b>Founder and Principal</div>
    <div class="s-o">4927 Corbel Street, Suite 300<br>Miami Beach, FL 33140</div>
    <div class="s-g">dana@harborlanternadvisory.example<br>harborlanternadvisory.example</div>
    <div class="r-y s-y">@msdanawhit</div>
  </div>
</article>
<div class="label" style="left:516px;top:222px;width:204px">Front Signature</div>

<!-- envelopes -->
<article class="item env" style="left:506px;top:256px;width:224px;height:106px">
  <div class="stripe"><span class="s-p"></span><span class="s-o"></span><span class="s-g"></span></div>
</article>
<article class="item env" style="left:496px;top:300px;width:224px;height:106px">
  <div class="brand" style="font-size:6px"><span class="dot" style="width:7px;height:7px"></span>Harbor Lantern</div>
  <div class="addr">4927 Corbel Street, Suite 300<br>Miami Beach, FL 33140</div>
  <div class="stripe"><span class="s-p"></span><span class="s-o"></span><span class="s-g"></span></div>
</article>
<div class="label" style="left:496px;top:412px;width:224px">Envelope Front</div>

<!-- fax sheet -->
<article class="item sheet fax" style="left:804px;top:36px;width:200px;height:380px">
  <div class="head">
    <div class="brand" style="font-size:7px"><span class="dot" style="width:8px;height:8px"></span>Harbor Lantern</div>
    <div class="addr">4927 Corbel Street, Suite 300<br>Miami Beach, FL 33140<br>dana@harborlanternadvisory.example</div>
  </div>
  <table>
    <tr><td>To:</td><td></td><td>From:</td><td></td></tr>
    <tr><td>Fax:</td><td></td><td>Pages:</td><td></td></tr>
    <tr><td>Phone:</td><td></td><td>Date:</td><td></td></tr>
    <tr><td>Re:</td><td></td><td></td><td></td></tr>
  </table>
  <div class="cm">Comments</div>
  <svg class="ring" width="80" height="80" viewBox="0 0 80 80" aria-hidden="true">
    <circle cx="40" cy="40" r="36" fill="none" stroke="#eeeeee" stroke-width="4"/>
  </svg>
  <div class="stripe"><span class="s-p"></span><span class="s-o"></span><span class="s-g"></span></div>
</article>
<div class="label" style="left:804px;top:422px;width:200px">Fax Sheet</div>

</body>
</html>
```